Natural Organic Cosmetics needs a packaging design

I need package design designs for an organic, natural, unrefined shea butter packaged in a pouch like the example below. The package design should express pure, organic, freshness, moisturizing and healthy. The package design should also reflect the benefits of the product listed below. The product will be called “ORGANIC SHEA BUTTER”
MEANING OF NAME: ZENO AFRICA" meaning to Come to Africa for your natural cosmetics
Logo Text/Brand Name:
“ZENO”
Logo Styles of Interest:
Elegance
Natural
Organic
Freshness
Unrefined
From a tree nut
Target Market:
General public
Must have:
KISS : Keep it simple stupid
Note: I have a shea nuts stock photo i can provide.
Dimension:W = 7.48 InchesH = 10.43 inches Added Thursday, January 14, 2016
Industry/Entity Type
Cosmetics

```html
<!DOCTYPE html>
<html lang="en">
<head>
<meta charset="utf-8">
<title>ZENO Shea Butter Pouch</title>
<link href="https://fonts.googleapis.com/css2?family=Open+Sans:wght@400;700;800&family=Dancing+Script:wght@700&display=swap" rel="stylesheet">
<style>
  :root {
    --backdrop: #d8cbbe;
    --pouch: #d3b898;
    --nut: #6b3419;
    --nut-dark: #4b1d12;
    --butter-light: #fbf6e6;
    --butter-mid: #efe3c2;
    --ink-light: #ffffff;
    --ink-soft: #f3ebe2;
  }
  html, body {
    margin: 0;
    padding: 0;
    width: 1200px;
    height: 900px;
    overflow: hidden;
    background: var(--backdrop);
  }
  .pouch-face {
    position: absolute;
    left: 380px;
    top: 88px;
    width: 465px;
    height: 682px;
    background: var(--pouch);
    overflow: hidden;
    font-family: "Open Sans", sans-serif;
  }
  .pouch-art {
    position: absolute;
    inset: 0;
  }
  .product-line {
    position: absolute;
    left: 0;
    width: 450px;
    top: 84px;
    text-align: center;
    color: var(--ink-light);
    font-weight: 800;
    font-size: 29px;
    letter-spacing: 2px;
    margin: 0;
  }
  .brand-name {
    position: absolute;
    left: 0;
    width: 450px;
    top: 100px;
    text-align: center;
    color: var(--ink-light);
    font-weight: 800;
    font-size: 94px;
    letter-spacing: -1px;
    line-height: 1.1;
    margin: 0;
  }
  .net-weight {
    position: absolute;
    left: 362px;
    top: 177px;
    font-size: 11px;
    color: var(--ink-light);
  }
  .usage-note {
    position: absolute;
    left: 430px;
    top: 190px;
    font-size: 12px;
    color: var(--ink-soft);
    letter-spacing: 0.5px;
    transform: rotate(-90deg);
    transform-origin: left top;
    white-space: nowrap;
    translate: 0 0;
  }
  .product-claims {
    position: absolute;
    left: 0;
    width: 455px;
    top: 626px;
    text-align: center;
    font-family: "Dancing Script", cursive;
    font-weight: 700;
    font-size: 20px;
    color: var(--ink-soft);
    letter-spacing: 0.5px;
  }
</style>
</head>
<body>
  <main class="pouch-face">
    <svg class="pouch-art" width="465" height="682" viewBox="0 0 465 682">
      <defs>
        <radialGradient id="butterTone" cx="45%" cy="40%" r="60%">
          <stop offset="0%" stop-color="var(--butter-light)"/>
          <stop offset="100%" stop-color="var(--butter-mid)"/>
        </radialGradient>
      </defs>
      <ellipse role="img" aria-label="Striped shea nut illustration" cx="40" cy="52" rx="75" ry="80" fill="var(--nut)"/>
      <ellipse role="img" aria-label="Striped shea nut illustration" cx="285" cy="20" rx="75" ry="70" fill="var(--nut)"/>
      <ellipse role="img" aria-label="Striped shea nut illustration" cx="435" cy="102" rx="45" ry="88" fill="var(--nut)"/>
      <ellipse role="img" aria-label="Striped shea nut illustration" cx="35" cy="362" rx="108" ry="155" fill="var(--nut)"/>
      <ellipse role="img" aria-label="Striped shea nut illustration" cx="305" cy="282" rx="78" ry="80" fill="var(--nut)"/>
      <ellipse role="img" aria-label="Striped shea nut illustration" cx="120" cy="632" rx="115" ry="110" fill="var(--nut)"/>
      <ellipse role="img" aria-label="Striped shea nut illustration" cx="410" cy="552" rx="85" ry="150" fill="var(--nut)"/>
      <circle role="img" aria-label="Photo of whipped raw shea butter" cx="235" cy="452" r="143" fill="url(#butterTone)"/>
    </svg>
    <p class="product-line">SHEA BUTTER</p>
    <h1 class="brand-name">ZENO</h1>
    <span class="net-weight">16oz.</span>
    <span class="usage-note">External use only</span>
    <p class="product-claims">Organic - Unrefined - Natural</p>
  </main>
</body>
</html>
```